Business Card - Professional Minimalist - Double sided

We appreciate minimalist logo/web/collateral designs that allow design to tell a story. We want to relay a professional image/approach but throwing in a splash of modern when we’re able so long as it’s not distracting. Think 75% classic corporate, 25% modern. Open to black or white design, not sure which might look the best.

Target Market(s)

Senior executives or related government affairs contacts within the agriculture, energy, and defense industries (i.e., potential clients) but located outside of Washington, DC. Most potential clients based in DC with be familiar with both of us and our shared history.

Industry/Entity Type

Consulting

Contact Information for Business Card

Name: Derek M. Holloway
Title: Co-Founder & Partner
Address: 418 Linwood Terrace NE | Suite 2260 | Washington, D.C. 20017
Phone: (202) 555-0148
Email: Derek@BrimleyHolloway.example

Font styles to use
Serif

Colors

Designer to choose only greyscale colors for use in the design.

Requirements
Must have
• Name: Derek M. Holloway
Phone: (202) 555-0148

```html
<!DOCTYPE html>
<html lang="en">
<head>
<meta charset="utf-8">
<title>Brimley Holloway Group – Business Card</title>
<link rel="stylesheet" href="https://fonts.googleapis.com/css2?family=Lato:wght@400;700&display=swap">
<style>
  :root {
    --page-bg: #d9d4cf;
    --card-top: #46423f;
    --card-bottom: #2e2b29;
    --text-soft: #8d8782;
    --text-name: #8a847f;
    --rule: #7a7570;
    --mark: #6f6a66;
  }
  * { margin: 0; padding: 0; box-sizing: border-box; }
  html, body {
    width: 1200px;
    height: 1047px;
    overflow: hidden;
    background: var(--page-bg);
    font-family: "Lato", "Helvetica Neue", Arial, sans-serif;
  }
  .card {
    position: absolute;
    left: 80px;
    top: 240px;
    width: 1040px;
    height: 566px;
    border-radius: 8px 48px 8px 48px;
    background: linear-gradient(160deg, var(--card-top) 0%, var(--card-bottom) 100%);
    box-shadow: 0 18px 40px rgba(0,0,0,0.25);
  }
  .company-name {
    position: absolute;
    left: 77px;
    top: 66px;
    font-size: 30px;
    font-weight: 400;
    letter-spacing: 2px;
    color: var(--text-soft);
    text-transform: uppercase;
  }
  .company-rule {
    position: absolute;
    left: 77px;
    top: 116px;
    width: 265px;
    height: 1px;
    background: var(--rule);
  }
  .person-name {
    position: absolute;
    left: 77px;
    top: 190px;
    font-size: 39px;
    font-weight: 700;
    color: var(--text-name);
  }
  .person-title {
    position: absolute;
    left: 78px;
    top: 243px;
    font-size: 25px;
    color: var(--text-soft);
  }
  .address {
    position: absolute;
    left: 72px;
    top: 294px;
    font-size: 26px;
    line-height: 34px;
    color: var(--text-soft);
    font-style: normal;
  }
  .contact-list {
    position: absolute;
    left: 72px;
    top: 410px;
    list-style: none;
  }
  .contact-item {
    display: flex;
    align-items: center;
    height: 38.5px;
    font-size: 25px;
    color: var(--text-soft);
  }
  .contact-icon {
    width: 24px;
    height: 24px;
    margin-right: 26px;
    flex: none;
  }
  .brand-square {
    position: absolute;
    left: 590px;
    top: 110px;
    width: 340px;
    height: 340px;
    border: 14px solid var(--mark);
  }
</style>
</head>
<body>
  <div class="card">
    <div class="company-name">Brimley Holloway Group</div>
    <div class="company-rule"></div>

    <h1 class="person-name">Derek M. Holloway</h1>
    <p class="person-title">Co-Founder &amp; Partner</p>

    <address class="address">
      418 Linwood Terrace NE<br>
      Suite 2260<br>
      Washington, D.C. 20017
    </address>

    <ul class="contact-list">
      <li class="contact-item">
        <svg class="contact-icon" viewBox="0 0 24 24" fill="none" stroke="#6f6a66" stroke-width="2" stroke-linecap="round" stroke-linejoin="round">
          <path d="M5 3h4l2 5-2.5 1.5a11 11 0 0 0 6 6L16 13l5 2v4a2 2 0 0 1-2 2A16 16 0 0 1 3 5a2 2 0 0 1 2-2z"/>
        </svg>
        (202) 555-0148
      </li>
      <li class="contact-item">
        <svg class="contact-icon" viewBox="0 0 24 24" fill="#6f6a66">
          <path d="M2 5h20v14H2z"/>
          <path d="M2 5l10 8 10-8" fill="none" stroke="#3a3735" stroke-width="1.6"/>
        </svg>
        Derek@BrimleyHolloway.example
      </li>
      <li class="contact-item">
        <svg class="contact-icon" viewBox="0 0 24 24" fill="none" stroke="#6f6a66" stroke-width="1.8">
          <circle cx="12" cy="12" r="9.5"/>
          <ellipse cx="12" cy="12" rx="4" ry="9.5"/>
          <path d="M2.5 12h19M4 7h16M4 17h16"/>
        </svg>
        www.BrimleyHolloway.example
      </li>
    </ul>

    <div class="brand-square" aria-hidden="true"></div>
  </div>
</body>
</html>
```